Camp Willowmere 2018

We need a postcard design to advertise our summer programs. We are a Christian camp with day camp and overnight camps.

Target Market(s)

parents of elementary age kids

Industry/Entity Type

Christian

Colors
ec1f27
f37122
faa54b
fbee3d
f78f20
f04a50
fbed22
fbee3e

Requirements
Must have
• Day Camp 2018 "Shine Bright Together"
• June 25 - August 24
• $135 per week
• Mon-Fri 8 am to 4 pm. Open to all kids entering grades 1 to 8. Day camp is chock full of activities like swimming, rock wall, archery, sports, crafts, air rifles and much more! Daily lunch and snack included. Before and after-care available at an extra rate.
• Register and pay in full by April 1st, save $270!
• Overnight Camp 2018
• July 15 - 21 & July 22 - 28
• $330 per week
• Open to all kids ages 8 to 14. Spend the week making new friends, sleeping in cabins, climbing the rock wall and swimming at the beach! Our guest speakers will lead twice daily chapel sessions that will challenge campers to grow in their faith.
• 41 Cedar Bluff Rd. Barrington, NH 03817
• 603-418-5296
• www.willowmere-example.org
Nice to have
• bright and colorful

```html
<!DOCTYPE html>
<html lang="en">
<head>
<meta charset="utf-8">
<title>Camp Willowmere 2018 Postcard</title>
<link rel="stylesheet" href="https://fonts.googleapis.com/css2?family=Montserrat:wght@200;700;800&family=Quicksand:wght@500;600&display=swap">
<style>
  :root {
    --card-orange: #f0821e;
    --brand-red: #ec1f27;
    --flame-orange: #f37122;
    --white: #ffffff;
    --stage: #ebe8e3;
    --photo-green: #7fae3e;
    --photo-light: #b9d27a;
    --photo-skin: #e8b9a4;
    --rule: rgba(255,255,255,0.8);
  }
  * { box-sizing: border-box; margin: 0; padding: 0; }
  html, body { width: 1200px; height: 600px; overflow: hidden; }
  body {
    background: var(--stage);
    position: relative;
    font-family: "Quicksand", sans-serif;
    color: var(--white);
  }
  .postcard {
    position: absolute;
    top: 128px;
    width: 518px;
    height: 344px;
    background: var(--card-orange);
    overflow: hidden;
    box-shadow: 0 3px 10px rgba(0,0,0,0.18);
  }
  .postcard--front { left: 52px; }
  .postcard--back { left: 614px; }

  /* Front */
  .front-photo { position: absolute; inset: 0; }
  .brand {
    display: flex;
    align-items: center;
    gap: 5px;
    font-family: "Montserrat", sans-serif;
    font-weight: 700;
    color: var(--brand-red);
    white-space: nowrap;
  }
  .brand__dot {
    width: 11px; height: 11px;
    border-radius: 50%;
    background: var(--brand-red);
    flex: none;
  }
  .postcard--front .brand {
    position: absolute;
    left: -4px; top: 46px;
    width: 120px;
    height: 16px;
    font-size: 11px;
    justify-content: center;
    transform: rotate(-45deg);
    transform-origin: 50% 50%;
  }
  .headline {
    position: absolute;
    left: 82px;
    bottom: 32px;
    transform: rotate(-45deg);
    transform-origin: 0 100%;
    font-family: "Montserrat", sans-serif;
    text-transform: uppercase;
    white-space: nowrap;
    line-height: 0.92;
  }
  .headline__light {
    display: block;
    font-weight: 200;
    font-size: 45px;
    letter-spacing: 0.5px;
  }
  .headline__bold {
    display: block;
    font-weight: 800;
    font-size: 46px;
    margin-left: 30px;
    margin-top: 2px;
  }

  /* Back */
  .back-grid {
    position: absolute;
    left: 28px; top: 14px;
    width: 462px;
    display: grid;
    grid-template-columns: 1fr 1fr;
  }
  .program {
    text-align: center;
    padding: 0 10px;
  }
  .program + .program { border-left: 1px solid var(--rule); }
  .program__title {
    font-family: "Montserrat", sans-serif;
    font-weight: 700;
    font-size: 12.5px;
    line-height: 1.3;
    text-transform: uppercase;
    height: 34px;
    display: flex; flex-direction: column; justify-content: center;
  }
  .program__text {
    font-size: 10.2px;
    line-height: 1.42;
    font-weight: 500;
    height: 112px;
    padding-top: 2px;
  }
  .program__details {
    border-top: 1px solid var(--rule);
    font-size: 10.5px;
    line-height: 1.55;
    padding-top: 3px;
    height: 66px;
    font-weight: 500;
  }
  .program + .program .program__details { margin-left: -10px; padding-left: 10px; }
  .program:first-child .program__details { margin-right: -10px; padding-right: 10px; }
  .offer { text-decoration: underline; }
  .offer strong { font-weight: 700; }
  .contact {
    position: absolute;
    left: 0; right: 0; top: 238px;
    text-align: center;
    font-size: 10.5px;
    line-height: 1.45;
    font-weight: 500;
    font-style: normal;
  }
  .back-footer {
    position: absolute;
    left: 0; right: 0; bottom: 0;
    height: 46px;
    background: var(--white);
    display: flex; align-items: center; justify-content: center;
  }
  .back-footer .brand { font-size: 12px; }
</style>
</head>
<body>
  <section class="postcard postcard--front">
    <svg class="front-photo" width="518" height="344" viewBox="0 0 518 344" role="img" aria-label="Photo of a smiling girl outdoors on a grassy field with another child behind her">
      <defs>
        <linearGradient id="fieldTone" x1="0" y1="0" x2="1" y2="1">
          <stop offset="0" stop-color="#7fae3e"/>
          <stop offset="0.55" stop-color="#b9d27a"/>
          <stop offset="1" stop-color="#e8b9a4"/>
        </linearGradient>
      </defs>
      <polygon points="433,0 518,0 518,344 89,344" fill="url(#fieldTone)"/>
    </svg>
    <div class="brand"><span class="brand__dot"></span>Camp Willowmere</div>
    <h1 class="headline">
      <span class="headline__light">Enjoy your</span>
      <span class="headline__light">childrens’</span>
      <span class="headline__bold">Happieness</span>
    </h1>
  </section>

  <section class="postcard postcard--back">
    <div class="back-grid">
      <article class="program">
        <h2 class="program__title">Day Camp 2018<br>«Shine Bright Together»</h2>
        <p class="program__text">Mon-Fri 8 am to 4 pm. Open to all kids entering grades 1 to 8. Day camp is chock full of activities like swimming, rock wall, archery, sports, crafts, air rifles and much more! Daily lunch and snack included. Before and after-care available at an extra rate.</p>
        <p class="program__details">June 25 - August 24<br>$135 per week<br><span class="offer">Register and pay in full by April 1st, save <strong>$270</strong></span>!</p>
      </article>
      <article class="program">
        <h2 class="program__title">Overnight Camp 2018</h2>
        <p class="program__text">Open to all kids ages 8 to 14. Spend the week making new friends, sleeping in cabins, climbing the rock wall and swimming at the beach! Our guest speakers will lead twice daily chapel sessions that will challenge campers to grow in their faith.</p>
        <p class="program__details">July 15 - 21 &amp; July 22 - 28<br>$330 per week</p>
      </article>
    </div>
    <address class="contact">
      41 Cedar Bluff Rd. Barrington, NH 03817<br>
      603-418-5296<br>
      www.willowmere-example.org
    </address>
    <footer class="back-footer">
      <div class="brand"><span class="brand__dot"></span>Camp Willowmere</div>
    </footer>
  </section>
</body>
</html>
```